Redesign/Update of www.nexorpartners.com

We are seeking a redesign for our casino afilliate website. At the moment, the design is dated and difficult to navigate, we are looking for a fresh, modern and attractive feel for the new homepage that will immediately grab potential affiliates, clearly states our pricing structures and makes it easy to register and become a customer.

Nexorpartners.com is the affiliate site for www.bluvekgaming.com.
Current site: www.nexorpartners.com

Similar sites that we like the style of:
http://www.quillorpartners.com/
http://www.zdreferrals.com/

Target Market(s)

Gambling Industry/Gambling Bloggers

Industry/Entity Type

Gambling

Coding

Coded - Design and coding required

Number of Pages Required

3 page

Font styles to use
Sans Serif

Colors
ec1f27
474747
d3d3d3
ffffff

Requirements
Must have
• A banner image
• A big call to action
• Three sections outline 'Why Join Nexorpartners'

```html
<!DOCTYPE html>
<html lang="en">
<head>
<meta charset="utf-8">
<title>Nexorpartners – Casino Affiliate Program</title>
<link href="https://fonts.googleapis.com/css2?family=Open+Sans:wght@400;600;700;800&display=swap" rel="stylesheet">
<style>
:root{
  --red:#ec1f27;
  --dark:#474747;
  --darker:#2e2e2e;
  --light:#d3d3d3;
  --white:#ffffff;
  --text:#6a6a6a;
}
*{box-sizing:border-box;margin:0;padding:0}
html,body{width:779px;height:1200px;overflow:hidden}
body{font-family:"Open Sans",Arial,sans-serif;background:var(--white);color:var(--text);font-size:9px;line-height:1.55}
a{color:inherit;text-decoration:none}

.site-header{height:42px;display:flex;align-items:center;justify-content:space-between;padding:0 62px 0 40px;border-bottom:1px solid #eee}
.brand{display:flex;align-items:center;gap:6px;color:var(--red);font-weight:700;font-size:15px}
.brand-mark{width:14px;height:14px;background:var(--red);border-radius:3px}
.main-nav{display:flex;gap:2px;font-size:8px;color:#555}
.main-nav a{padding:6px 9px}
.main-nav a.active{color:var(--red);border-bottom:2px solid var(--red)}

.hero{position:relative;height:372px;background:#0b0b0b;overflow:hidden}
.hero-photo{position:absolute;inset:0;background:radial-gradient(circle at 22% 45%,#5a1518 0,#2a0b0c 22%,#0d0d0d 48%,#050505 100%)}
.hero-copy{position:absolute;left:428px;top:188px;width:260px;color:var(--white)}
.hero-title{font-size:31px;font-weight:800;line-height:1.1;letter-spacing:-.5px}
.hero-title span{color:var(--red)}
.hero-copy p{font-size:8px;margin-top:6px;color:#ddd}
.hero-badge{position:absolute;left:464px;top:82px;width:58px;height:58px;border-radius:50%;background:var(--red);border:3px solid #e8c25a}

.why{display:flex;justify-content:space-between;padding:38px 60px 0 62px;height:258px}
.why-text{width:440px}
.why h2{font-size:17px;color:#333;font-weight:600}
.why .lead{font-size:8px;margin:2px 0 8px}
.btn{display:inline-block;background:var(--red);color:var(--white);font-weight:600}
.btn-lg{font-size:9px;padding:12px 20px;margin-top:20px}
.promo{width:160px;height:140px;background:#0a0a0a;border:2px solid #222;color:var(--white);text-align:center;padding-top:20px;font-weight:800;text-transform:uppercase}
.promo .big{font-size:32px;line-height:1;color:#f1e6c8}
.promo .mid{font-size:13px;line-height:1.2}
.promo .amp{font-size:20px;color:#e8c25a;line-height:1.1}
.promo .small{font-size:8px;font-weight:600}

.services{text-align:center;padding-top:6px}
.section-title{display:flex;align-items:center;justify-content:center;gap:14px;font-size:19px;color:#333;font-weight:600}
.section-title::before,.section-title::after{content:"";width:190px;height:1px;background:var(--light)}
.services .lead{font-size:8px;margin-top:2px}
.cards{display:flex;gap:32px;justify-content:center;margin-top:18px}
.card{width:195px;height:142px;border:1px solid var(--light);padding:14px 22px}
.card svg{display:block;margin:0 auto 6px}
.card h3{font-size:9.5px;color:var(--red);font-weight:600;line-height:1.3}
.card p{font-size:7px;margin:5px 0 8px;line-height:1.5}
.btn-sm{font-size:7px;padding:4px 10px}

.login-bar{display:flex;gap:28px;justify-content:center;margin-top:26px}
.login-bar .field{width:145px;height:19px;border:1px solid var(--light);font-size:7px;color:#aaa;padding:4px 6px}
.login-bar .btn{width:64px;height:19px;font-size:8px;text-align:center;line-height:19px}

.site-footer{position:absolute;left:0;top:898px;width:779px;height:302px;background:var(--dark);color:#bbb}
.footer-main{display:flex;justify-content:space-between;padding:28px 60px 0 62px;height:236px}
.footer-main h4{color:var(--white);font-size:9.5px;font-weight:600}
.footer-main p{font-size:7px;width:420px;margin-top:4px}
.footer-brand{color:var(--white);font-weight:700;font-size:16px;margin-top:4px}
.footer-bar{height:66px;background:var(--darker);display:flex;align-items:center;justify-content:space-between;padding:0 62px;font-size:7px}
.footer-bar nav a{margin-right:10px}
.socials{display:flex;gap:6px}
.socials span{width:14px;height:14px;border-radius:50%;background:#555}
</style>
</head>
<body>
<header class="site-header">
  <a class="brand" href="#"><span class="brand-mark"></span>Nexorpartners</a>
  <nav class="main-nav">
    <a class="active" href="#">Home</a><a href="#">Commissions</a><a href="#">Contact Us</a><a href="#">Help</a><a href="#">Terms &amp; Conditions</a>
  </nav>
</header>

<section class="hero">
  <div class="hero-photo" role="img" aria-label="Close-up of a casino roulette wheel with ball in dark red light"></div>
  <div class="hero-badge" role="img" aria-label="Fast payout badge"></div>
  <div class="hero-copy">
    <h1 class="hero-title">Nexorpartners <span>Casino</span></h1>
    <p>Join a partner program built for growth and earn generous revenue share on every player you refer to our casino.</p>
  </div>
</section>

<section class="why">
  <div class="why-text">
    <h2>Why Join Nexorpartners</h2>
    <p class="lead">Partner with a trusted brand and grow your income.</p>
    <p>We give affiliates the tools, tracking and support they need to turn traffic into steady income. Our team works with bloggers and publishers of every size, offering fair terms, clear reporting and fast payments month after month.</p>
    <a class="btn btn-lg" href="#">Become a Nexorpartners</a>
  </div>
  <div class="promo">
    <div class="big">£500</div>
    <div class="mid">Deposit Bonus</div>
    <div class="amp">&amp;</div>
    <div class="mid">50 Free Spins</div>
    <div class="small">On Crimson Reels</div>
  </div>
</section>

<section class="services">
  <h2 class="section-title">What We Do</h2>
  <p class="lead">Everything you need to promote our brand and earn more.</p>
  <div class="cards">
    <article class="card">
      <svg width="30" height="30" viewBox="0 0 30 30"><circle cx="15" cy="15" r="14" fill="none" stroke="#ec1f27" stroke-width="1.5"/><path d="M9 14h3v8H9zM13 14l3-6c1.5 0 2 1 1.6 2.5L17 13h4c1 0 1.6.8 1.4 1.7l-1.2 5.6c-.2.9-.9 1.7-1.8 1.7H13z" fill="#ec1f27"/></svg>
      <h3>Great Commission<br>Structure</h3>
      <p>Earn a strong revenue share on every player you refer, with tiers that reward growth.</p>
      <a class="btn btn-sm" href="#">Find Out More</a>
    </article>
    <article class="card">
      <svg width="30" height="30" viewBox="0 0 30 30"><circle cx="15" cy="15" r="14" fill="none" stroke="#ec1f27" stroke-width="1.5"/><rect x="9" y="10" width="12" height="11" fill="none" stroke="#ec1f27" stroke-width="1.5"/><path d="M9 13h12M12 8v3M18 8v3" stroke="#ec1f27" stroke-width="1.5"/></svg>
      <h3>We Pay on<br>Time</h3>
      <p>Payments are processed on schedule every month, so you always know when to expect them.</p>
      <a class="btn btn-sm" href="#">Find Out More</a>
    </article>
    <article class="card">
      <svg width="30" height="30" viewBox="0 0 30 30"><circle cx="15" cy="15" r="14" fill="none" stroke="#ec1f27" stroke-width="1.5"/><text x="15" y="20.5" text-anchor="middle" font-family="Open Sans,Arial,sans-serif" font-size="15" font-weight="700" fill="#ec1f27">$</text></svg>
      <h3>Your balance is updated<br>in real time</h3>
      <p>Track clicks, sign ups and earnings live from your personal dashboard at any time.</p>
      <a class="btn btn-sm" href="#">Find Out More</a>
    </article>
  </div>
  <form class="login-bar">
    <div class="field">Enter User Name</div>
    <div class="field">Enter Password</div>
    <div class="field">Enter Affiliate ID</div>
    <a class="btn" href="#">Login</a>
  </form>
</section>

<footer class="site-footer">
  <div class="footer-main">
    <div>
      <h4>Register now and start earning cash from your visitors!</h4>
      <p>As a Nexorpartners affiliate you promote one of the most exciting online casinos and earn commission on every real money player you send. Sign up takes a few minutes, our managers are ready to help, and every tool you need is waiting inside. Contact us at any time for more details.</p>
    </div>
    <div class="footer-brand">Bluvek Gaming</div>
  </div>
  <div class="footer-bar">
    <nav><a href="#">Nexorpartners 2016</a><a href="#">Home</a><a href="#">Help</a><a href="#">Contact</a><a href="#">Commissions</a><a href="#">Sign Up</a><a href="#">Terms &amp; Conditions</a></nav>
    <div class="socials"><span></span><span></span><span></span></div>
  </div>
</footer>
</body>
</html>
```